Business Card Design job - Tessa's Business Cards

Simple elegant feminine design - Going out on my own as a Mortgage Broker.
My thoughts are the following details on the Front, middle of the card possibly? Phone and email smaller font than my name?
Tessa Marwick
Finance Specialist
p: 0438 217 905
e: tessa@marwickfinance.com.au
Bottom of the card
residential / commercial / equipment
I would like the Font in Rose Gold maybe white or black background? or Possibly a stone grey - are you able to do a few options? I'd like them embossed
Then I had an idea as a simple logo as per the attached if you get the idea in my scribble, my initials, capital T attached to a small m that leads/follows into a circle? Thicker Font In Rose Gold, middle of the card at the back.
Very open to ideas though and what colour you think would look better with the Rose Gold.
Thanks so much for your help, I am not very creative and savvy with this stuff :-)
Industry/Entity Type
Finance
Contact Information for Business Card
Tessa Marwick
p: 0438 217 905
Look and feel
Each slider illustrates characteristics of the customer's brand and the style your logo design should communicate.

```html
<!DOCTYPE html>
<html lang="en">
<head>
<meta charset="utf-8">
<title>Tessa Marwick – Business Cards</title>
<link rel="stylesheet" href="https://fonts.googleapis.com/css2?family=Cormorant+Garamond:wght@500&display=swap">
<style>
  :root {
    --backdrop: #ebebea;
    --card-stone: #9c9d9d;
    --rose-gold: #dcb89b;
    --card-shadow: rgba(0, 0, 0, 0.18);
  }
  * { margin: 0; padding: 0; box-sizing: border-box; }
  html, body {
    width: 1200px;
    height: 900px;
    overflow: hidden;
    background: var(--backdrop);
  }
  .canvas {
    position: relative;
    width: 1200px;
    height: 900px;
    font-family: "Cormorant Garamond", Georgia, serif;
    font-weight: 500;
    color: var(--rose-gold);
  }
  .card {
    position: absolute;
    top: 307px;
    width: 500px;
    height: 286px;
    background: var(--card-stone);
    box-shadow: 0 6px 18px var(--card-shadow);
  }
  .card--back { left: 70px; }
  .card--front { left: 630px; }

  .brand-mark {
    display: flex;
    align-items: center;
    gap: 10px;
    white-space: nowrap;
  }
  .brand-mark__circle {
    flex: none;
    border: 2px solid var(--rose-gold);
    border-radius: 50%;
  }
  .card--back .brand-mark {
    position: absolute;
    left: 50%;
    top: 50%;
    transform: translate(-50%, -50%);
    font-size: 34px;
    gap: 16px;
  }
  .card--back .brand-mark__circle { width: 40px; height: 40px; }

  .card--front .brand-mark {
    position: absolute;
    left: 22px;
    top: 50%;
    transform: translateY(-50%);
    font-size: 17px;
  }
  .card--front .brand-mark__circle { width: 20px; height: 20px; border-width: 1.5px; }

  .divider {
    position: absolute;
    left: 200px;
    top: 40px;
    width: 1.5px;
    height: 206px;
    background: var(--rose-gold);
  }
  .contact {
    position: absolute;
    left: 228px;
    top: 72px;
    line-height: 1.25;
  }
  .contact__name {
    font-size: 27px;
    font-variant: small-caps;
    letter-spacing: 0.04em;
  }
  .contact__role { font-size: 16px; margin-bottom: 14px; }
  .contact__line { font-size: 16px; }
</style>
</head>
<body>
<main class="canvas">
  <section class="card card--back" aria-label="Card back">
    <div class="brand-mark">
      <span class="brand-mark__circle"></span>
      <span class="brand-mark__name">Tessa Marwick</span>
    </div>
  </section>

  <section class="card card--front" aria-label="Card front">
    <div class="brand-mark">
      <span class="brand-mark__circle"></span>
      <span class="brand-mark__name">Tessa Marwick</span>
    </div>
    <div class="divider"></div>
    <div class="contact">
      <p class="contact__name">Tessa Marwick</p>
      <p class="contact__role">Finance Specialist</p>
      <p class="contact__line">P: 0438 217 905</p>
      <p class="contact__line">E: tessa.marwick@finmail.net</p>
    </div>
  </section>
</main>
</body>
</html>
```